Brindle Logistics Business Card Design

We are a trucking and warehousing company. We run freight in the US manly from the Pacific NW to TX and back up the the PNW. We also do warehousing where we store, move, and distribute freight. Looking for a clean and modern design of business card. We would like to look rich and elegant. Attached is our logo.

Industry/Entity Type

Trucking Company

Contact Information for Business Card

Looking for a clean and modern design of business card. We would like to look rich and elegant.

Font styles to use
Sans Serif

Colors

Designer to choose colors to be used in the design.

Requirements
Must have
• logo but it should not dominate the card
Should not have
• logo should not dominate the card

```html
<!DOCTYPE html>
<html lang="en">
<head>
<meta charset="UTF-8">
<title>Brindle Logistics Business Card</title>
<link rel="stylesheet" href="https://fonts.googleapis.com/css2?family=Roboto:wght@400;500;700&family=Roboto+Condensed:wght@700&display=swap">
<style>
  :root {
    --backdrop: #2b2b2d;
    --card: #1f1f21;
    --ink: #f4f4f4;
    --muted: #d9d9d9;
    --blue: #1a8fd8;
    --orange: #f0a21c;
    --divider: #5c5c60;
  }
  * { margin: 0; padding: 0; box-sizing: border-box; }
  html, body {
    width: 1200px; height: 900px; overflow: hidden;
    background: var(--backdrop);
    font-family: "Roboto", Arial, sans-serif;
    color: var(--ink);
  }
  .stage {
    position: relative; width: 1200px; height: 900px;
  }
  .card {
    position: absolute; left: 280px; width: 640px; height: 365px;
    background: var(--card);
    box-shadow: 0 12px 30px rgba(0,0,0,0.45);
  }
  .card--front { top: 70px; }
  .card--back { top: 465px; }

  /* Front */
  .brand {
    position: absolute; top: 105px; left: 0; width: 100%;
    display: flex; justify-content: center; align-items: center; gap: 16px;
  }
  .brand__dot {
    width: 34px; height: 34px; border-radius: 50%; background: var(--blue);
  }
  .brand__name {
    font-family: "Roboto", Arial, sans-serif;
    font-weight: 700; font-size: 40px; letter-spacing: 2px;
    color: var(--ink); line-height: 1; text-transform: uppercase;
  }
  .front__web {
    position: absolute; top: 228px; left: 0; width: 100%; text-align: center;
    font-size: 15px; letter-spacing: 9px; color: var(--muted);
  }

  /* Back */
  .person {
    position: absolute; top: 100px; left: 50px; width: 235px; text-align: right;
  }
  .person__name {
    font-family: "Roboto Condensed", Arial, sans-serif;
    font-weight: 700; font-size: 36px; color: var(--blue); line-height: 1;
    letter-spacing: 0.5px;
  }
  .person__title {
    font-family: "Roboto Condensed", Arial, sans-serif;
    font-weight: 700; font-size: 17px; color: var(--orange); margin-top: 4px;
  }
  .back__divider {
    position: absolute; left: 305px; top: 60px; width: 1px; height: 125px;
    background: var(--divider);
  }
  .contacts {
    position: absolute; left: 325px; top: 68px; list-style: none;
  }
  .contacts li {
    display: flex; align-items: center; gap: 10px;
    font-size: 16px; font-weight: 500; line-height: 23px; color: var(--ink);
  }
  .contacts svg { width: 14px; height: 14px; fill: var(--blue); flex: none; }
  .address {
    position: absolute; left: 50px; bottom: 85px;
    display: flex; align-items: center; gap: 6px;
    font-size: 17px; font-weight: 500; color: var(--ink);
  }
  .address svg { width: 14px; height: 18px; fill: var(--blue); }
</style>
</head>
<body>
<div class="stage">
  <section class="card card--front">
    <div class="brand">
      <span class="brand__dot"></span>
      <span class="brand__name">Brindle Logistics, LLC</span>
    </div>
    <p class="front__web">www.brindlelogistics.com</p>
  </section>

  <section class="card card--back">
    <div class="person">
      <p class="person__name">DANIEL REYES</p>
      <p class="person__title">CEO/FOUNDER</p>
    </div>
    <div class="back__divider"></div>
    <ul class="contacts">
      <li>
        <svg viewBox="0 0 24 24" aria-hidden="true"><path d="M6.6 10.8c1.4 2.8 3.8 5.1 6.6 6.6l2.2-2.2c.3-.3.7-.4 1-.2 1.1.4 2.3.6 3.6.6.6 0 1 .4 1 1V20c0 .6-.4 1-1 1C10.6 21 3 13.4 3 4c0-.6.4-1 1-1h3.5c.6 0 1 .4 1 1 0 1.3.2 2.5.6 3.6.1.3 0 .7-.2 1z"/></svg>
        555 214 7360
      </li>
      <li>
        <svg viewBox="0 0 24 24" aria-hidden="true"><path d="M7 1h10c1.1 0 2 .9 2 2v18c0 1.1-.9 2-2 2H7c-1.1 0-2-.9-2-2V3c0-1.1.9-2 2-2zm0 3v14h10V4H7zm5 15.5a1 1 0 100 2 1 1 0 000-2z"/></svg>
        555 309 8142
      </li>
      <li>
        <svg viewBox="0 0 24 24" aria-hidden="true"><path d="M6 2h12v5H6zM4 8h16c1.1 0 2 .9 2 2v7h-4v5H6v-5H2v-7c0-1.1.9-2 2-2zm4 8v4h8v-4H8z"/></svg>
        555 472 6018
      </li>
      <li>
        <svg viewBox="0 0 24 24" aria-hidden="true"><path d="M2 5h20v14H2zm2 2v.5l8 5 8-5V7l-8 5z"/></svg>
        info@brindlelogistics.com
      </li>
      <li>
        <svg viewBox="0 0 24 24" aria-hidden="true"><path d="M12 2a10 10 0 100 20 10 10 0 000-20zm-1 17.9A8 8 0 014.1 10l4.9 4.9v1c0 1.1.9 2 2 2v2zm6.9-2.5c-.3-.8-1-1.4-1.9-1.4h-1v-3c0-.6-.4-1-1-1H8v-2h2c.6 0 1-.4 1-1V7h2c1.1 0 2-.9 2-2v-.4a8 8 0 012.9 12.8z"/></svg>
        www.brindlelogistics.com
      </li>
    </ul>
    <p class="address">
      <svg viewBox="0 0 14 18" aria-hidden="true"><path d="M7 0a7 7 0 00-7 7c0 5 7 11 7 11s7-6 7-11a7 7 0 00-7-7zm0 9.5A2.5 2.5 0 117 4.5a2.5 2.5 0 010 5z"/></svg>
      2140 Cedar Hollow Road, Tacoma, Washington 98402
    </p>
  </section>
</div>
</body>
</html>
```